Brisa pet parlour. I need a tag for a vans trail hauler 3400

It is a mobile dog grooming. For pets. I provide bathing and haircutting services for pets at the door of your house. In the city of Miami Florida. Therefore everything must be in English. The
Images that I am attaching with the poodle are my logo. And so I want to label the vans. I need a design that looks elegant and not too loaded

Target Market(s)

Upper class adults.

Industry/Entity Type

Pet Care

Font styles to use
Serif
Script

Colors

Designer to choose only greyscale colors for use in the design.

Requirements
Must have
• The big phone number on all 4 sides of the vans! 8084719265 I would like to use black and white colors. I would like an option with a white background and another with. The black background. Like the images I'm appending
You must have my website. Www.brisapetparlour.com

The logos of chatzoop and Talkwire
Text indicating that they can send text

Something elegant and classic.

It should include that they can find me on snapfolio, Kinpage, zorbit, and Revo.
The logos of each social network.
Nice to have
• Slogan. "One goal, one passion, one dream,
Excellence in pet care "

```html
<!DOCTYPE html>
<html lang="en">
<head>
<meta charset="utf-8">
<title>Brisa Pet Parlour – Van Wrap</title>
<link rel="stylesheet" href="https://fonts.googleapis.com/css2?family=Cormorant+Garamond:wght@500&family=Oswald:wght@400;500;600&display=swap">
<style>
  :root {
    --ink: #0d0d0d;
    --paper: #ffffff;
    --stage: #ececec;
    --band-mid: #2a2a2a;
    --rule: #c9c9c9;
    --soft: #5a5a5a;
  }
  * { box-sizing: border-box; margin: 0; padding: 0; }
  html, body { width: 1200px; height: 1200px; overflow: hidden; }
  body { background: var(--stage); position: relative; font-family: "Oswald", sans-serif; color: var(--ink); }

  .panel { position: absolute; background: var(--paper); border: 1px solid var(--rule); overflow: hidden; }
  .mark-circle { position: absolute; border-radius: 50%; background: var(--ink); }
  .brand-name { position: absolute; font-family: "Cormorant Garamond", serif; font-weight: 500; color: var(--ink); white-space: nowrap; line-height: 1; }
  .brand-tagline { position: absolute; font-family: "Oswald", sans-serif; font-weight: 400; text-transform: uppercase; color: var(--soft); white-space: nowrap; }
  .phone { position: absolute; font-weight: 600; color: var(--ink); white-space: nowrap; }
  .chat-list { position: absolute; display: flex; flex-direction: column; gap: 6px; }
  .chat-item { display: flex; align-items: center; gap: 6px; font-weight: 500; color: var(--ink); white-space: nowrap; }
  .chat-item .dot { border-radius: 50%; background: var(--ink); flex: none; }
  .band { position: absolute; left: 0; right: 0; background: var(--ink); color: var(--paper); }
  .band-line { position: absolute; left: 0; right: 0; height: 2px; background: var(--paper); }
  .slogan, .services { position: absolute; color: var(--paper); letter-spacing: 1.5px; white-space: nowrap; text-transform: uppercase; font-weight: 500; }
  .services-box { position: absolute; background: var(--band-mid); }
  .website { position: absolute; letter-spacing: 2px; text-transform: uppercase; white-space: nowrap; font-weight: 500; }
  .socials { position: absolute; display: flex; gap: 8px; }
  .social { display: flex; align-items: center; gap: 4px; font-weight: 500; white-space: nowrap; }
  .social .sq { flex: none; }

  /* side */
  .side { left: 50px; top: 60px; width: 1100px; height: 500px; }
  .side .mark-circle { left: 50px; top: 40px; width: 150px; height: 150px; }
  .side .brand-name { left: 230px; top: 58px; font-size: 84px; }
  .side .brand-tagline { left: 236px; top: 150px; font-size: 20px; letter-spacing: 6px; }
  .side .chat-list { left: 50px; top: 232px; }
  .side .chat-item { font-size: 17px; }
  .side .chat-item .dot { width: 14px; height: 14px; }
  .side .phone { left: 180px; top: 200px; font-size: 86px; letter-spacing: 9px; line-height: 1.2; }
  .side .website { right: 40px; top: 246px; font-size: 13px; }
  .side .socials { right: 40px; top: 272px; }
  .side .social { font-size: 12px; }
  .side .social .sq { width: 12px; height: 12px; background: var(--ink); }
  .side .band { top: 340px; height: 160px; }
  .side .band-line { top: 14px; }
  .side .slogan { left: 270px; top: 36px; font-size: 24px; }
  .side .services-box { left: 250px; top: 84px; width: 560px; height: 44px; }
  .side .services { left: 290px; top: 88px; font-size: 24px; letter-spacing: 2.5px; }

  /* rear */
  .rear { left: 90px; top: 640px; width: 420px; height: 460px; }
  .rear .mark-circle { left: 170px; top: 24px; width: 80px; height: 80px; }
  .rear .brand-name { left: 0; right: 0; top: 118px; text-align: center; font-size: 40px; }
  .rear .brand-tagline { left: 0; right: 0; top: 164px; text-align: center; font-size: 11px; letter-spacing: 3px; }
  .rear .chat-list { left: 16px; top: 204px; gap: 3px; }
  .rear .chat-item { font-size: 11px; gap: 4px; }
  .rear .chat-item .dot { width: 9px; height: 9px; }
  .rear .phone { left: 92px; top: 196px; font-size: 38px; letter-spacing: 4px; line-height: 1.2; }
  .rear .band { top: 280px; height: 180px; }
  .rear .services { left: 18px; top: 16px; font-size: 12px; }
  .rear .socials { right: 18px; top: 46px; gap: 6px; }
  .rear .social { font-size: 10px; color: var(--paper); }
  .rear .social .sq { width: 10px; height: 10px; background: var(--paper); }
  .rear .website { right: 18px; top: 70px; font-size: 9px; color: var(--paper); letter-spacing: 1.5px; }
  .rear .slogan { left: 0; right: 0; top: 112px; text-align: center; font-size: 12px; letter-spacing: 0.8px; }

  /* front */
  .front { left: 600px; top: 640px; width: 510px; height: 460px; }
  .front .chat-list { left: 40px; top: 30px; gap: 3px; }
  .front .chat-item { font-size: 11px; gap: 4px; }
  .front .chat-item .dot { width: 9px; height: 9px; }
  .front .phone { left: 118px; top: 18px; font-size: 40px; letter-spacing: 4px; line-height: 1.2; }
  .front .services { color: var(--ink); left: 120px; top: 74px; font-size: 15px; letter-spacing: 2px; }
  .front .plate { position: absolute; left: 70px; top: 290px; width: 370px; height: 90px; border: 1px solid var(--rule); background: var(--paper); }
  .front .mark-circle { left: 22px; top: 18px; width: 54px; height: 54px; }
  .front .brand-name { left: 92px; top: 18px; font-size: 34px; }
  .front .brand-tagline { left: 94px; top: 56px; font-size: 10px; letter-spacing: 3px; }
</style>
</head>
<body>

<section class="panel side" aria-label="Side wrap">
  <div class="mark-circle"></div>
  <div class="brand-name">Brisa Pet Parlour</div>
  <div class="brand-tagline">Grooming at your door</div>
  <div class="chat-list">
    <div class="chat-item"><span class="dot"></span>chatzoop</div>
    <div class="chat-item"><span class="dot"></span>Talkwire</div>
  </div>
  <div class="phone">808.471.9265</div>
  <div class="website">www.brisapetparlour.com</div>
  <div class="socials">
    <span class="social"><span class="sq"></span>Kinpage</span>
    <span class="social"><span class="sq"></span>snapfolio</span>
    <span class="social"><span class="sq"></span>zorbit</span>
    <span class="social"><span class="sq"></span>Revo</span>
  </div>
  <div class="band">
    <div class="band-line"></div>
    <div class="slogan">One goal, one passion, one dream, excellence in pet care</div>
    <div class="services-box"></div>
    <div class="services">Profesional pet grooming/ pet dental</div>
  </div>
</section>

<section class="panel rear" aria-label="Rear wrap">
  <div class="mark-circle"></div>
  <div class="brand-name">Brisa Pet Parlour</div>
  <div class="brand-tagline">Grooming at your door</div>
  <div class="chat-list">
    <div class="chat-item"><span class="dot"></span>chatzoop</div>
    <div class="chat-item"><span class="dot"></span>Talkwire</div>
  </div>
  <div class="phone">808.471.9265</div>
  <div class="band">
    <div class="services">Pet grooming/ pet dental</div>
    <div class="socials">
      <span class="social"><span class="sq"></span>Kinpage</span>
      <span class="social"><span class="sq"></span>snapfolio</span>
      <span class="social"><span class="sq"></span>zorbit</span>
      <span class="social"><span class="sq"></span>Revo</span>
    </div>
    <div class="website">www.brisapetparlour.com</div>
    <div class="slogan">One goal, one passion, one dream, excellence in pet care</div>
  </div>
</section>

<section class="panel front" aria-label="Front wrap">
  <div class="chat-list">
    <div class="chat-item"><span class="dot"></span>chatzoop</div>
    <div class="chat-item"><span class="dot"></span>Talkwire</div>
  </div>
  <div class="phone">808.471.9265</div>
  <div class="services">Pet grooming/ pet dental</div>
  <div class="plate">
    <div class="mark-circle"></div>
    <div class="brand-name">Brisa Pet Parlour</div>
    <div class="brand-tagline">Grooming at your door</div>
  </div>
</section>

</body>
</html>
```